Help a start up law firm make an impression! - Website

We are a property development and conveyancing law firm looking for some to design our website. The initial brief is for 6 pages with scope for on-going work.

Law firms are traditionally quite conservative and we want to break the mold. We want to come across as fun and modern, while still being professional.

A good example is https://quorrantlaw.com.au/. It's professional yet modern.
Updates

Another good site I like in the same industry: https://www.tindalemarshconveyancing.com.au/

Target Market(s)

Tech savy home buyers and sellers - generally 30 to 50 years old

Industry/Entity Type

Law Firm

Coding

Coded - Design and coding required

Number of Pages Required

5+ page

Font styles to use
Other font styles liked:
• No idea

Colors
f04a50

Requirements
Must have
• The elements set out in the design brief document

```html
<!DOCTYPE html>
<html lang="en">
<head>
<meta charset="utf-8">
<title>Contact Us – Harlowe Law</title>
<link rel="stylesheet" href="https://fonts.googleapis.com/css2?family=Montserrat:wght@400;500;600;700&family=Oswald:wght@400&family=Domine:wght@700&display=swap">
<style>
:root{
  --brand:#d63d58;
  --navy:#1c2f4d;
  --navy-deep:#13233d;
  --ink:#2b2b2b;
  --muted:#555b66;
  --paper:#f6f6f6;
  --card:#ffffff;
  --line:#d9d9d9;
  --bar:#e4e4e4;
  --social:#7a7d82;
}
*{box-sizing:border-box;margin:0;padding:0}
html,body{width:734px;height:1200px;overflow:hidden}
body{position:relative;font-family:"Montserrat",sans-serif;color:var(--ink);background:var(--paper)}
.abs{position:absolute}

/* hero */
.hero{left:0;top:0;width:734px;height:203px;background:linear-gradient(100deg,#3c4a60 0%,#24375a 40%,#1b2d4c 70%,#2a3c5c 100%)}
.hero-photo{left:0;top:0;width:340px;height:203px;background:radial-gradient(ellipse at 35% 45%,rgba(150,140,140,.35),rgba(30,45,75,0) 70%)}
.brand-name{font-family:"Montserrat",sans-serif;font-weight:700;letter-spacing:.2px}
.hero .brand-name{left:15px;top:20px;font-size:21px;color:#fff}
.nav{left:214px;top:27px;display:flex;gap:13px;font-family:"Oswald",sans-serif;font-size:10.5px;color:#fff}
.nav .current{color:var(--brand)}
.nav-phone{left:590px;top:22px;display:flex;align-items:center;gap:6px;font-family:"Oswald",sans-serif;font-size:18px;color:#fff}
.hero-rule{left:0;top:62px;width:734px;height:1px;background:rgba(255,255,255,.15)}
.hero-title{left:0;top:78px;width:734px;text-align:center;font-family:"Domine",serif;font-size:39px;color:#fff;letter-spacing:2px}
.hero-sub{left:0;top:149px;width:734px;text-align:center;font-size:12px;font-weight:500;color:#fff}

/* info cards */
.card{top:254px;width:163px;height:110px;background:var(--card);border:1px solid var(--line);box-shadow:0 2px 0 #e2e2e2;text-align:center}
.card-icon{margin:13px auto 0;width:40px;height:40px;border-radius:50%;background:var(--brand);display:flex;align-items:center;justify-content:center}
.card-title{margin-top:10px;font-size:11px;font-weight:600;color:var(--brand)}
.card-text{font-size:9.5px;line-height:12px;color:var(--muted)}

/* map */
.map{left:0;top:412px;width:734px;height:240px;background:linear-gradient(180deg,#e6e6e6,#dcdcdc)}

/* contact form */
.touch{left:0;top:652px;width:734px;height:351px;background:linear-gradient(160deg,#2a3d5c 0%,var(--navy) 45%,var(--navy-deep) 100%)}
.touch-heading{left:0;top:712px;width:734px;text-align:center;font-size:24px;letter-spacing:1.5px;color:#fff;font-weight:400}
.touch-heading b{color:var(--brand);font-weight:700}
.field{background:#fff;border-radius:2px;font-size:7px;color:#8a8a8a;padding:8px 7px;letter-spacing:.3px}
.send{left:129px;top:934px;width:476px;height:26px;background:var(--brand);border-radius:2px;color:#fff;font-size:7.5px;font-weight:700;text-align:center;line-height:26px;letter-spacing:.4px}

/* footer */
.footer{left:0;top:1003px;width:734px;height:157px;background:var(--paper)}
.foot-head{font-size:11px;font-weight:600;color:var(--brand);letter-spacing:.5px}
.foot-head::after{content:"";display:block;width:28px;height:2px;background:var(--brand);margin-top:4px}
.foot-links{list-style:none;font-size:9.5px;line-height:15.4px;color:var(--muted)}
.foot-item{display:flex;gap:8px;font-size:9.5px;line-height:11.5px;color:var(--muted)}
.footer .brand-name{left:490px;top:1050px;font-size:22px;color:var(--ink)}
.bottom-bar{left:0;top:1160px;width:734px;height:40px;background:var(--bar)}
.copyright{left:60px;top:1174px;font-size:8.5px;color:#333;letter-spacing:.3px}
.social{top:1168px;width:20px;height:20px;border-radius:50%;background:var(--social)}
</style>
</head>
<body>

<header>
  <div class="abs hero"></div>
  <div class="abs hero-photo" role="img" aria-label="Photo of a smiling woman talking on a mobile phone against a dark city backdrop"></div>
  <div class="abs brand-name">Harlowe Law</div>
  <nav class="abs nav"><span>Home</span><span>Conveyancing</span><span>Property Development</span><span>News &amp; Knowledge</span><span>About us</span><span class="current">Contact us</span></nav>
  <div class="abs nav-phone">
    <svg width="14" height="14" viewBox="0 0 24 24"><path fill="#d63d58" d="M6.6 10.8a15.1 15.1 0 0 0 6.6 6.6l2.2-2.2a1 1 0 0 1 1-.25 11.4 11.4 0 0 0 3.6.57 1 1 0 0 1 1 1V20a1 1 0 0 1-1 1A17 17 0 0 1 3 4a1 1 0 0 1 1-1h3.5a1 1 0 0 1 1 1c0 1.25.2 2.45.57 3.57a1 1 0 0 1-.25 1z"/></svg>
    <span>(07) 3198 4420</span>
  </div>
  <div class="abs hero-rule"></div>
  <h1 class="abs hero-title">CONTACT US</h1>
  <p class="abs hero-sub">Our team of experts are ready to hear from you</p>
</header>

<section>
  <div class="abs card" style="left:29px">
    <div class="card-icon"><svg width="20" height="20" viewBox="0 0 24 24"><path fill="#fff" d="M6.6 10.8a15.1 15.1 0 0 0 6.6 6.6l2.2-2.2a1 1 0 0 1 1-.25 11.4 11.4 0 0 0 3.6.57 1 1 0 0 1 1 1V20a1 1 0 0 1-1 1A17 17 0 0 1 3 4a1 1 0 0 1 1-1h3.5a1 1 0 0 1 1 1c0 1.25.2 2.45.57 3.57a1 1 0 0 1-.25 1z"/></svg></div>
    <div class="card-title">Phone Number</div>
    <div class="card-text">(07) 3198 4420</div>
  </div>
  <div class="abs card" style="left:201px">
    <div class="card-icon"><svg width="20" height="16" viewBox="0 0 20 16"><rect x="1" y="1" width="18" height="14" fill="none" stroke="#fff" stroke-width="1.6"/><path d="M1 1l9 8 9-8" fill="none" stroke="#fff" stroke-width="1.6"/></svg></div>
    <div class="card-title">Email Address</div>
    <div class="card-text">mail@harlowelaw.com.au</div>
  </div>
  <div class="abs card" style="left:373px">
    <div class="card-icon"><svg width="16" height="22" viewBox="0 0 16 22"><path fill="#fff" d="M8 0a8 8 0 0 0-8 8c0 6 8 14 8 14s8-8 8-14a8 8 0 0 0-8-8zm0 11a3 3 0 1 1 0-6 3 3 0 0 1 0 6z"/></svg></div>
    <div class="card-title">Address</div>
    <div class="card-text">Level 1, 842 Kessler Road,<br>Ashbury, Queensland 4019</div>
  </div>
  <div class="abs card" style="left:545px">
    <div class="card-icon"><svg width="22" height="22" viewBox="0 0 22 22"><circle cx="11" cy="11" r="9" fill="none" stroke="#fff" stroke-width="2"/><path d="M11 5v6l4 2" fill="none" stroke="#fff" stroke-width="2"/></svg></div>
    <div class="card-title">Office Hours</div>
    <div class="card-text">Monday to Friday<br>9am to 5pm</div>
  </div>
</section>

<div class="abs map" role="img" aria-label="Street map showing the office location on Kessler Road, Ashbury"></div>

<section>
  <div class="abs touch"></div>
  <svg class="abs" style="left:352px;top:676px" width="32" height="32" viewBox="0 0 32 32" fill="none" stroke="#fff" stroke-width="1.3"><rect x="5" y="2" width="18" height="16"/><path d="M8 6h12M8 9h12M8 12h8"/><path d="M2 14v16h26V14M2 30l11-9M28 30l-11-9"/></svg>
  <svg class="abs" style="left:190px;top:722px" width="356" height="10"><line x1="5" y1="5" x2="72" y2="5" stroke="#fff" stroke-width="1"/><circle cx="5" cy="5" r="2.5" fill="none" stroke="#fff"/><line x1="288" y1="5" x2="351" y2="5" stroke="#fff" stroke-width="1"/><circle cx="351" cy="5" r="2.5" fill="none" stroke="#fff"/></svg>
  <h2 class="abs touch-heading">GET IN <b>TOUCH</b></h2>
  <div class="abs field" style="left:129px;top:758px;width:231px;height:26px">FIRST NAME*</div>
  <div class="abs field" style="left:376px;top:758px;width:229px;height:26px">LAST NAME*</div>
  <div class="abs field" style="left:129px;top:800px;width:231px;height:26px">E-MAIL ADDRESS*</div>
  <div class="abs field" style="left:376px;top:800px;width:229px;height:26px">PHONE NUMBER*</div>
  <div class="abs field" style="left:129px;top:842px;width:476px;height:78px">MESSAGE</div>
  <div class="abs send">SEND NOW</div>
  <svg class="abs" style="left:327px;top:981px" width="80" height="23" viewBox="0 0 80 23"><path d="M0 23c14 0 16-20 40-20s26 20 40 20z" fill="#f6f6f6"/><path d="M35 12l5 5 5-5" fill="none" stroke="#d63d58" stroke-width="1.5"/></svg>
</section>

<footer>
  <div class="abs footer"></div>
  <div class="abs foot-head" style="left:60px;top:1027px">QUICK LINKS</div>
  <ul class="abs foot-links" style="left:60px;top:1052px"><li>Home</li><li>Conveyancing</li><li>Property Development</li><li>News &amp; Knowledge</li><li>About us</li><li>Contact us</li></ul>
  <div class="abs foot-head" style="left:260px;top:1027px">CONTACT US</div>
  <div class="abs foot-item" style="left:242px;top:1054px"><svg width="10" height="13" viewBox="0 0 16 22"><path fill="#d63d58" d="M8 0a8 8 0 0 0-8 8c0 6 8 14 8 14s8-8 8-14a8 8 0 0 0-8-8zm0 11a3 3 0 1 1 0-6 3 3 0 0 1 0 6z"/></svg><span>Level 1, 842 Kessler Road,<br>Ashbury, Queensland 4019</span></div>
  <div class="abs foot-item" style="left:242px;top:1089px"><svg width="11" height="11" viewBox="0 0 24 24"><circle cx="12" cy="12" r="12" fill="#d63d58"/><path fill="#fff" d="M8.5 11a8 8 0 0 0 4.5 4.5l1.3-1.3 2.2.6v2.2a8 8 0 0 1-10-10h2.2l.6 2.2z"/></svg><span>(07) 3198 4420</span></div>
  <div class="abs foot-item" style="left:242px;top:1116px"><svg width="11" height="11" viewBox="0 0 24 24"><circle cx="12" cy="12" r="12" fill="#d63d58"/><rect x="6" y="8" width="12" height="8" fill="none" stroke="#fff" stroke-width="1.5"/><path d="M6 8l6 5 6-5" fill="none" stroke="#fff" stroke-width="1.5"/></svg><span>mail@harlowelaw.com.au</span></div>
  <div class="abs brand-name">Harlowe Law</div>
  <div class="abs bottom-bar"></div>
  <div class="abs copyright">© COPYRIGHT - 2017 &nbsp;|&nbsp; ALL RIGHTS RESERVED</div>
  <div class="abs social" style="left:576px" role="img" aria-label="Social profile link"></div>
  <div class="abs social" style="left:602px" role="img" aria-label="Social profile link"></div>
  <div class="abs social" style="left:628px" role="img" aria-label="Social profile link"></div>
  <div class="abs social" style="left:654px" role="img" aria-label="Social profile link"></div>
</footer>

</body>
</html>
```